We provide Professional DJ Service in different genres of music ranging from Latin to Hip/Hop R&B/TOP 40 etc...we also help promote DJ/Music/Artists events Internationally. I am looking for the main color of my business to be fluorescent lime green with some traces of 'smurf' blue. Maybe military feel attached to it as well as I am active duty military and all of my DJ's are either active or retired. That would be our main focus. We can do anything from Formal military balls to backyard parties We are also mobile and can be hired by local clubs/pubs/bars.

Target Market(s)

Military Community/Events/ Local nightclubs/pubs/bars looking to hire professional DJ's.

Industry/Entity Type

Entertainment

Contact Information for Business Card

Brevane Entertainment (Professional DJ Service/Event Promoter)/email:dorkabrevane@quelmail.example/ Plazzly logo with address or scan directly to my page. (Plazzly-search Brevane Entertainment) Tomas 'DJ Kestrel' Brevane. Owner/DJ/Promoter

Font styles to use
Serif

Colors
acd136
33a6d7

Requirements
Must have
• Looking for on back of card Plazzly logo and scanbar leading directly to my PZ page...if not possible then Plazzly.com search Brevane Entertainment (or both).
Nice to have
• The attachment that I sent has my logo that I would like to use, however it is not a finished product. Is this only for business cards layout or also to spruce up or make my logo better? It's the Brevane

```html
<!DOCTYPE html>
<html lang="en">
<head>
<meta charset="utf-8">
<title>Brevane Entertainment – Business Card</title>
<link rel="stylesheet" href="https://fonts.googleapis.com/css2?family=Orbitron:wght@700;900&family=Quicksand:wght@500;600;700&display=swap">
<style>
  :root {
    --backdrop: #a9a7ab;
    --lime: #b4d65a;
    --lime-bright: #c3e06a;
    --olive: #5d7a3b;
    --forest: #1f4a2c;
    --forest-deep: #173a22;
    --ink: #101510;
    --white: #ffffff;
  }
  * { margin: 0; padding: 0; box-sizing: border-box; }
  html, body {
    width: 1200px; height: 800px; overflow: hidden;
    background: var(--backdrop);
  }
  .stage {
    position: relative; width: 1200px; height: 800px;
    display: flex; align-items: center; justify-content: center; gap: 60px;
  }
  .card {
    position: relative; width: 520px; height: 297px; overflow: hidden;
    box-shadow: 0 6px 18px rgba(0,0,0,0.25);
  }
  .card svg.card-art { position: absolute; inset: 0; width: 100%; height: 100%; }

  /* Front: striped face with brand name */
  .brand-mark {
    position: absolute; left: 50%; top: 50%; transform: translate(-50%, -50%);
    font-family: "Orbitron", sans-serif; font-weight: 900;
    font-size: 17px; letter-spacing: 0.5px; color: var(--white);
    white-space: nowrap;
  }

  /* Back: contact face */
  .title {
    position: absolute; left: 205px; top: 98px;
    font-family: "Orbitron", sans-serif; font-weight: 900;
    font-size: 17px; color: var(--ink); letter-spacing: 0.5px;
    white-space: nowrap;
  }
  .tagline {
    position: absolute; left: 205px; top: 122px;
    font-family: "Quicksand", sans-serif; font-weight: 600;
    font-size: 13px; color: var(--forest); letter-spacing: 0.6px;
  }
  .person-name {
    position: absolute; left: 200px; top: 168px;
    font-family: "Quicksand", sans-serif; font-weight: 700;
    font-size: 18px; color: var(--lime-bright); letter-spacing: 0.8px;
    white-space: nowrap;
  }
  .person-role {
    position: absolute; left: 238px; top: 194px;
    font-family: "Quicksand", sans-serif; font-weight: 600;
    font-size: 10.5px; color: var(--lime-bright);
    padding-bottom: 3px; border-bottom: 1.5px solid var(--lime-bright);
    width: 150px;
  }
  .contact-list {
    position: absolute; left: 150px; top: 226px; list-style: none;
    font-family: "Quicksand", sans-serif; font-weight: 600;
    font-size: 13px; color: var(--lime-bright); letter-spacing: 0.4px;
  }
  .contact-list li { display: flex; align-items: center; gap: 8px; height: 24px; }
  .contact-icon { width: 13px; height: 13px; flex: none; }
</style>
</head>
<body>
<main class="stage">

  <!-- Front face -->
  <section class="card card-front" aria-label="Business card front">
    <svg class="card-art" viewBox="0 0 520 297" aria-hidden="true">
      <rect width="520" height="297" fill="var(--lime)"/>
      <rect y="0" width="520" height="32" fill="var(--olive)"/>
      <rect y="92" width="520" height="60" fill="var(--olive)"/>
      <rect y="208" width="520" height="32" fill="var(--olive)"/>
      <rect y="270" width="520" height="27" fill="var(--olive)"/>
      <circle cx="260" cy="148" r="62" fill="var(--forest)"/>
    </svg>
    <p class="brand-mark">BREVANE ENTERTAINMENT</p>
  </section>

  <!-- Back face -->
  <section class="card card-back" aria-label="Business card back">
    <svg class="card-art" viewBox="0 0 520 297">
      <rect width="520" height="297" fill="var(--lime)"/>
      <rect y="150" width="520" height="147" fill="var(--forest)"/>
      <defs>
        <radialGradient id="facet-tone" cx="40%" cy="40%" r="70%">
          <stop offset="0" stop-color="#6f8f5a"/>
          <stop offset="0.6" stop-color="#2f5a36"/>
          <stop offset="1" stop-color="var(--forest-deep)"/>
        </radialGradient>
      </defs>
      <circle cx="40" cy="40" r="150" fill="url(#facet-tone)" stroke="#d9e8b8" stroke-width="2"
              role="img" aria-label="Faceted green crystal texture"/>
      <circle cx="468" cy="64" r="30" fill="var(--forest)" aria-hidden="true"/>
    </svg>
    <h1 class="title">BREVANE ENTERTAINMENT</h1>
    <p class="tagline">Professional DJ Service/Event Promoter</p>
    <p class="person-name">Tomas 'DJ Kestrel' Brevane</p>
    <p class="person-role">Owner/DJ/Promoter</p>
    <ul class="contact-list">
      <li>
        <svg class="contact-icon" viewBox="0 0 13 13" aria-hidden="true">
          <rect x="0.5" y="2.5" width="12" height="8" rx="1" fill="var(--lime-bright)"/>
          <path d="M1 3 L6.5 7.5 L12 3" fill="none" stroke="var(--forest)" stroke-width="1.2"/>
        </svg>
        dorkabrevane@quelmail.example
      </li>
      <li>
        <svg class="contact-icon" viewBox="0 0 13 13" aria-hidden="true">
          <rect x="0.5" y="0.5" width="12" height="12" rx="1.5" fill="var(--lime-bright)"/>
        </svg>
        /brevanemusic
      </li>
    </ul>
  </section>

</main>
</body>
</html>
```